Dental Design, very professional and noticable

Copperleaf Ridge Dental Surgery is based in Pelican Waters. We are a fast growing dental surgery and are looking for some professional business cards to send to patients.
We would like to see a design that is Vertical and uses the colours Soft Blue, Silver, White and Black. Maybe a full blue side with moto and details on back? Any other ideas or colours that you may think will make the card look unique is fine.
We need all details on the card that are listed above

Target Market(s)

Families, Retired, Other Professionals and Businesses

Industry/Entity Type

Dental

Contact Information for Business Card

Copperleaf Ridge Dental Surgery
Family, Cosmetic, Preventative
Dr. Owen Farrish
Dental Surgeon
BDS (Adel) FAE FADI FICD FPFA
phone: (07)54810296
fax: (07)54926170
email: copperleafridgedental@quillpost.net
http://copperleafridgedental.quillpost.net/

Logo Text

Logo styles of interest
Abstract Logo
Requirements
Must have
• Vertical, Vibrant but Professional, Rounded Edges, Logo on front and back of card (different colours on each side)
Nice to have
• One side completely blue (not sure what shade) with logo and moto on bottom
Other side white, with blue or different coloured logo with details in black and silver?
Logo should show half circle with 1 end as arrow symbolizing pelican waters canal also a magnifine glass also half circled with 1 end as arrow. Any other ideas are welcome.
Should not have
• A tooth. A smile. Toothbrush or Toothpaste. Cornered edges.

```html
<!DOCTYPE html>
<html lang="en">
<head>
<meta charset="utf-8">
<title>Copperleaf Ridge Dental Surgery – Business Card</title>
<link rel="stylesheet" href="https://fonts.googleapis.com/css2?family=Cabin:wght@400;600;700&display=swap">
<style>
  :root {
    --stage: #2b2b2b;
    --navy: #0f2d4b;
    --gold: #8f7326;
    --white: #ffffff;
    --silver: #e9e9e9;
    --ink: #0f2d4b;
  }
  html, body {
    margin: 0;
    padding: 0;
    width: 1200px;
    height: 900px;
    overflow: hidden;
    background: var(--stage);
    font-family: "Cabin", "Gill Sans", sans-serif;
  }
  .canvas {
    position: relative;
    width: 1200px;
    height: 900px;
  }
  .card {
    position: absolute;
    top: 150px;
    width: 380px;
    height: 600px;
    border-radius: 34px;
    overflow: hidden;
    box-shadow: 0 16px 36px rgba(0,0,0,0.5);
  }
  .card--back {
    left: 170px;
    background: var(--navy);
  }
  .card--front {
    left: 650px;
    background: linear-gradient(160deg, var(--white) 0%, var(--silver) 100%);
  }
  .brand {
    display: flex;
    align-items: center;
    justify-content: center;
    gap: 12px;
    color: var(--gold);
    font-weight: 600;
    text-align: center;
  }
  .brand__dot {
    flex: none;
    width: 22px;
    height: 22px;
    border-radius: 50%;
    background: var(--gold);
  }
  .brand__name {
    line-height: 1.1;
  }
  .card--back .brand {
    position: absolute;
    top: 230px;
    left: 0;
    right: 0;
    font-size: 30px;
  }
  .motto {
    position: absolute;
    bottom: 44px;
    left: 0;
    right: 0;
    text-align: center;
    color: var(--gold);
    font-size: 19px;
    letter-spacing: 0.5px;
  }
  .card--front .brand {
    margin-top: 58px;
    font-size: 25px;
  }
  .details {
    text-align: center;
    color: var(--ink);
    margin-top: 44px;
  }
  .details__name {
    font-size: 25px;
    letter-spacing: 0.5px;
  }
  .details__role {
    font-size: 18px;
    font-weight: 700;
  }
  .details__credentials {
    font-size: 17px;
    margin-top: 2px;
    letter-spacing: 0.5px;
  }
  .contact {
    margin-top: 24px;
    text-align: center;
    color: var(--ink);
  }
  .contact__label {
    font-size: 12px;
    letter-spacing: 1px;
    text-transform: uppercase;
    margin-top: 8px;
  }
  .contact__value {
    font-size: 22px;
    letter-spacing: 0.5px;
  }
  .contact__value--email {
    font-size: 16px;
  }
  .web-band {
    position: absolute;
    bottom: 0;
    left: 0;
    right: 0;
    height: 72px;
    background: var(--navy);
    color: var(--gold);
    font-size: 16px;
    letter-spacing: 0.5px;
    display: flex;
    align-items: center;
    justify-content: center;
  }
</style>
</head>
<body>
<main class="canvas">
  <section class="card card--back" aria-label="Card back">
    <div class="brand">
      <span class="brand__dot"></span>
      <span class="brand__name">Copperleaf Ridge<br>Dental Surgery</span>
    </div>
    <p class="motto">Family, Cosmetic, Preventative</p>
  </section>

  <section class="card card--front" aria-label="Card front">
    <div class="brand">
      <span class="brand__dot"></span>
      <span class="brand__name">Copperleaf Ridge<br>Dental Surgery</span>
    </div>
    <div class="details">
      <div class="details__name">Dr. Owen Farrish</div>
      <div class="details__role">Dental Surgeon</div>
      <div class="details__credentials">BDS (Adel) FAE FADI FICD FPFA</div>
    </div>
    <div class="contact">
      <div class="contact__label">Phone</div>
      <div class="contact__value">(07) 548 102 96</div>
      <div class="contact__label">Fax</div>
      <div class="contact__value">(07) 549 261 70</div>
      <div class="contact__label">Email</div>
      <div class="contact__value contact__value--email">copperleafridgedental@quillpost.net</div>
    </div>
    <div class="web-band">www.copperleafridgedental.quillpost.net</div>
  </section>
</main>
</body>
</html>
```